Need 8.5" x 11" as well as large 11"x17" Posters for our upcoming event

Please include LOGOs in poster
Main logo is Harborview Teen Circle of PL

All high school age faith groups are invited to come and join with 150 to 175 other high school students from various faith traditions to participate in the Harborview Teen Circle of Pine Lakes‘s Annual Kindred Voices Gathering. More than ever, our county and world need young leaders who are willing to learn from each other and build stronger communities!

KINDRED GATHERING
The purpose of this Interfaith Youth Forum is to bring together young people from diverse ethnic, cultural, and religious backgrounds, and to engage them in dialogue. True dialogue is a conversation on a common subject between two or more persons of differing points of view and/or backgrounds. We feel that this commitment to dialogue will affect relationships in a constructive way in our places of worship and in our community.
The forum itself involves having eight religiously diverse high school-age students, one adult, and youth leader around each table to discuss common questions. Our youth leaders act as facilitators, but it is stressed that it is the students we want to hear from.
RSVP for our KINDRED GATHERING before February 18th, 2018
FORUM QUESTIONS Available online at http://htcpl-example.org/home/kindred-fair/

Target Market(s)

Houses of worship, community leaders, High School Students

Industry/Entity Type

Non-Profit

Font styles to use
Serif

Colors
cfdeed
0255a3
f78f20
f37122
f68d4d
faa54b
ffcf3e
ffc214
34a6d7

Requirements
Must have
• Harborview Teen Circle of Pine Lakes's 14th Annual Kindred Gathering & Fair
• TEENS EXPRESSING THEIR FAITH THROUGH ART, MUSIC, AND DIALOGUE
• THIS YEAR'S THEME: “Who Are You?”
• Sunday, March 11th, 2018 11:00am-5:00pm
• Congregation Ner Adamah
• 4187 W Larkmont Rd. Santa Ana, CA 92705
• Email: htcplorg@mailbox-example.com
• Website: HTCPL-example.org
• Facebook: Harborview Teen Circle of Pine Lakes
Nice to have
• Descriptions provided in word doc
Should not have
• -

```html
<!DOCTYPE html>
<html lang="en">
<head>
<meta charset="utf-8">
<title>Kindred Gathering &amp; Fair Poster</title>
<link rel="stylesheet" href="https://fonts.googleapis.com/css2?family=Montserrat:wght@600;700;800;900&family=Mulish:wght@600;700&display=swap">
<style>
  :root{
    --page-bg:#ffffff;
    --panel-dark:#3b3b3d;
    --panel-gray:#bdbfc1;
    --orange:#f37122;
    --orange-light:#faa54b;
    --orange-deep:#c9581c;
    --yellow:#ffcf3e;
    --yellow-edge:#ffc214;
    --blue:#0255a3;
    --sky:#34a6d7;
    --ink:#1e1e1e;
    --white:#ffffff;
    --cream:#fff6d8;
  }
  *{box-sizing:border-box;margin:0;padding:0}
  html,body{width:1200px;height:1200px;overflow:hidden;background:var(--page-bg)}
  .poster{position:absolute;left:137px;top:0;width:926px;height:1200px;overflow:hidden;font-family:"Mulish",sans-serif}
  .side-panel{position:absolute;left:0;top:0;width:333px;height:1127px;background:var(--panel-dark)}
  .content-panel{position:absolute;left:333px;top:0;width:593px;height:1127px;background:var(--panel-gray)}
  .photo-frames{position:absolute;left:0;top:0;width:333px;height:1127px}
  .theme{position:absolute;left:43px;top:342px;color:var(--white);font-family:"Montserrat",sans-serif}
  .theme-label{font-size:23px;font-weight:800;letter-spacing:-0.3px}
  .theme-title{font-size:98px;font-weight:900;line-height:76px;margin-top:24px;letter-spacing:-1px}
  .theme-title span{display:block}
  .theme-title .spaced{letter-spacing:14px}
  .brand-row{position:absolute;left:500px;top:30px;display:flex;align-items:center;gap:8px}
  .brand-mark{width:38px;height:38px;border-radius:50%;background:var(--white)}
  .brand-name{font-size:11px;font-weight:700;color:var(--blue);width:92px;line-height:13px}
  .partner-badge{width:40px;height:22px;background:var(--white)}
  .partner-stack{display:flex;flex-direction:column;gap:6px}
  .event-banner{position:absolute;left:316px;top:120px;width:610px;height:54px;background:var(--orange);color:var(--cream);
    font-family:"Montserrat",sans-serif;font-weight:800;font-size:16.5px;line-height:21px;padding:6px 10px 0 14px;text-transform:uppercase}
  .tagline{position:absolute;left:358px;top:188px;font-family:"Montserrat",sans-serif;font-weight:800;font-size:13.5px;
    letter-spacing:-0.4px;white-space:nowrap;color:var(--ink)}
  .section-bar{position:absolute;left:343px;width:583px;height:37px;font-family:"Montserrat",sans-serif;font-weight:800;font-size:24px;
    line-height:37px;padding-left:12px;letter-spacing:0.5px}
  .section-bar.yellow{background:var(--yellow);color:var(--panel-dark);border-left:8px solid var(--yellow-edge)}
  .section-bar.blue{background:var(--blue);color:var(--white);border-left:8px solid var(--sky)}
  .section-text{position:absolute;left:353px;width:560px;font-size:14.2px;line-height:25px;color:var(--ink);font-weight:700}
  .section-text .single-line{white-space:nowrap;font-size:13.4px;letter-spacing:-0.2px}
  .footer{position:absolute;left:0;top:1127px;width:926px;height:73px;background:var(--orange-deep);color:var(--white);
    font-family:"Mulish",sans-serif;font-weight:700;font-size:15px}
  .footer-item{position:absolute;display:flex;align-items:flex-start;gap:8px;line-height:18px;white-space:nowrap}
  .footer-item svg{flex:none;margin-top:1px}
  .footer-item.contact{font-size:14.5px;letter-spacing:-0.2px}
  .fb-square{width:14px;height:14px;background:var(--white);flex:none;margin-top:2px}
</style>
</head>
<body>
<main class="poster">
  <section class="side-panel"></section>
  <section class="content-panel"></section>

  <svg class="photo-frames" viewBox="0 0 333 1127" width="333" height="1127">
    <defs>
      <linearGradient id="frameOrange" x1="0" y1="0" x2="1" y2="1">
        <stop offset="0" stop-color="#f78f20"/><stop offset="1" stop-color="#f37122"/>
      </linearGradient>
      <linearGradient id="frameYellow" x1="0" y1="0" x2="1" y2="1">
        <stop offset="0" stop-color="#ffc214"/><stop offset="1" stop-color="#f78f20"/>
      </linearGradient>
      <linearGradient id="photoStage" x1="0" y1="0" x2="0" y2="1">
        <stop offset="0" stop-color="#8c2a2e"/><stop offset="0.55" stop-color="#5a4a58"/><stop offset="1" stop-color="#b59a86"/>
      </linearGradient>
      <linearGradient id="photoGroup" x1="0" y1="0" x2="0" y2="1">
        <stop offset="0" stop-color="#cfc4b8"/><stop offset="0.5" stop-color="#6f8fb8"/><stop offset="1" stop-color="#8a8a8a"/>
      </linearGradient>
    </defs>
    <polygon points="12,82 298,62 292,295 18,308" fill="url(#frameOrange)"/>
    <rect x="40" y="100" width="236" height="176" fill="url(#photoStage)" role="img" aria-label="Group photo of the youth participants on stage"/>
    <polygon points="12,680 290,670 294,925 18,912" fill="url(#frameYellow)"/>
    <rect x="44" y="704" width="222" height="180" fill="url(#photoGroup)" role="img" aria-label="Photo of teen youth leaders standing together"/>
  </svg>

  <div class="theme">
    <p class="theme-label">This Year’s Theme:</p>
    <h2 class="theme-title"><span>WHO</span><span class="spaced">ARE</span><span>YOU?</span></h2>
  </div>

  <div class="brand-row">
    <div class="brand-mark"></div>
    <p class="brand-name">Harborview Teen Circle of PL</p>
    <div class="partner-stack"><div class="partner-badge"></div><div class="partner-badge"></div></div>
  </div>

  <h1 class="event-banner">Harborview Teen Circle of Pine Lakes's 14th Annual Kindred Gathering and Fair</h1>
  <p class="tagline">TEENS EXPRESSING THEIR FAITH THROUGH ART, MUSIC AND DIALOGUE</p>

  <h3 class="section-bar yellow" style="top:237px">KINDRED GATHERING</h3>
  <div class="section-text" style="top:282px">
    <p>This purpose of this Interfaith Youth Forum is to bring together young people from diverse ethnic, cultural, and religious backgrounds, and to engage them in dialogue. True dialogue is a conversation on a common subject between two or more persons of differing points of view and/or backgrounds. We feel that this commitment to dialogue will affect relationships in a constructive way in our places of worship and in our community. The forum itself involves having eight religiously diverse high school - age students, one adult, and youth leader around each table to discuss common questions. Our youth leaders act as facilitators, but it is stressed that it is the students we want to hear from.</p>
    <p>RSVP for our KINDRED GATHERING before February 18th, 2018</p>
    <p class="single-line">FORUM QUESTIONS : Available online at http://htcpl-example.org/home/kindred-fair/</p>
  </div>

  <h3 class="section-bar blue" style="top:620px">FAITH FESTIVAL</h3>
  <div class="section-text" style="top:664px">
    <p>The forum will include our Faith Festival portion of the program which families of the participants are welcomed to join. The Festival will include musical performances of all types from diverse religious communities. The differing performing arts include but are not limited to singing, dancing, instrumental music, storytelling, etc.</p>
    <p>To participate in our Faith Festival (Music, Song, Dance) ,</p>
    <p>RSVP by February 11th, 2018</p>
  </div>

  <h3 class="section-bar yellow" style="top:873px">ART GALLERY</h3>
  <div class="section-text" style="top:918px">
    <p>This event will include and Art Gallery display of students’ work, highlighting their expressions of faith, and artwork promoting learning, understanding, leadership, and service. Art includes any painting, illustration, sculpture, photography or other visual art.</p>
    <p>Art Work for our Art Gallery must be submitted by: March 3rd, 2018</p>
  </div>

  <footer class="footer">
    <div class="footer-item" style="left:17px;top:10px">
      <svg width="18" height="16" viewBox="0 0 18 16"><polygon points="9,0 18,5 0,5" fill="#fff"/><rect x="2" y="6" width="2.5" height="7" fill="#fff"/><rect x="7.7" y="6" width="2.5" height="7" fill="#fff"/><rect x="13.5" y="6" width="2.5" height="7" fill="#fff"/><rect x="0" y="14" width="18" height="2" fill="#fff"/></svg>
      <p>Congregation Ner Adamah<br>4187 W Larkmont Rd. Santa Ana, CA 92705</p>
    </div>
    <div class="footer-item" style="left:21px;top:48px">
      <div class="fb-square"></div>
      <p>Harborview Teen Circle of Pine Lakes</p>
    </div>
    <div class="footer-item" style="left:410px;top:16px">
      <svg width="16" height="16" viewBox="0 0 16 16"><circle cx="8" cy="8" r="7" fill="none" stroke="#fff" stroke-width="2"/><path d="M8 4v4.5h3" fill="none" stroke="#fff" stroke-width="1.8"/></svg>
      <p>11:00am - 5 : 00pm</p>
    </div>
    <div class="footer-item" style="left:410px;top:46px">
      <svg width="16" height="16" viewBox="0 0 16 16"><rect x="1" y="3" width="14" height="12" fill="none" stroke="#fff" stroke-width="2"/><rect x="1" y="3" width="14" height="4" fill="#fff"/></svg>
      <p>Sunday, March 11th, 2018</p>
    </div>
    <div class="footer-item contact" style="left:645px;top:16px">
      <svg width="16" height="16" viewBox="0 0 16 16"><circle cx="8" cy="8" r="7" fill="none" stroke="#fff" stroke-width="1.8"/><ellipse cx="8" cy="8" rx="3" ry="7" fill="none" stroke="#fff" stroke-width="1.3"/><path d="M1 8h14" stroke="#fff" stroke-width="1.3"/></svg>
      <p>HTCPL-example.org</p>
    </div>
    <div class="footer-item contact" style="left:645px;top:46px">
      <svg width="16" height="16" viewBox="0 0 16 16"><rect x="1" y="3" width="14" height="10" fill="none" stroke="#fff" stroke-width="1.8"/><path d="M1 3l7 6 7-6" fill="none" stroke="#fff" stroke-width="1.5"/></svg>
      <p>htcplorg@mailbox-example.com</p>
    </div>
  </footer>
</main>
</body>
</html>
```